Re-design UI/UX for Online movie website

We need a stunning design for our online movie website www.vormalite.com

KALDORVUE is an online platform for the presentation of all visual art forms, particularly movies, feature films, short films, documentaries, game shows, reality shows, serials and traditional art forms of different languages for our international audience to indulge in.

We want a design & layout similar to leading online movie streaming websites such as Brimcast , Tavelo Crest , PLUMA BAY

Target Market(s)

Worldwide

Industry/Entity Type

Movie

Number of Pages Required

5+ page

Requirements
Must have
• Look & Feel - These are some of the suggestion. Please feel free to add as per industry standards. Be as creative as possible. The website needs to be really attractive. Movie listing , categories etc., should be easy to navigate
• 1 Text could be justified in all the pages
• 2 Font color may be changed to white color to be more visible.
• 3 Headings to be in Red color instead of Orange color. As Red will match the logo color as well
• 4 Heading to be consistent everywhere. Example in About us page " About us" font is capital, white in color and larger than the other 2 headings on the same page.
• 5 Chatterly, quibbr and Snapgrove links to be added
• 6 Menu options could be in white or red color to be more visible. Current grey color is looking dull.
• 8 One more menu tab to be included on the top named "Movies" or "Browse movies" . Under Browse Movies, add multilevel menu "New Releases" "Short Films" "Kaldorvue Originals" "Library" "All Movies" . Later categories like Comedy, Thriller etc, can be added
• 9 Add “Watch movie” or “Watch Trailer” on the banner Images
• 10 Give “back to home link” on all subpages
• 11 The Grid format showing movie thumbnails can be made better with border (red or white)

```html
<!DOCTYPE html>
<html lang="en">
<head>
<meta charset="utf-8">
<title>KALDORVUE — We Screen Your Dreams</title>
<link rel="stylesheet" href="https://fonts.googleapis.com/css2?family=Roboto:wght@400;500;700;900&family=Open+Sans:wght@400;600;700&display=swap">
<style>
:root{
  --red:#d0171b;
  --red-dark:#b31216;
  --white:#ffffff;
  --text:#e8e8e8;
  --muted:#bdbdbd;
  --bg-a:#141414;
  --bg-b:#0d0d0d;
  --footer:#0a0a0a;
  --rule:#2c2c2c;
}
*{box-sizing:border-box;margin:0;padding:0}
html,body{width:1200px;height:3232px;overflow:hidden;background:var(--bg-b);color:var(--white);font-family:"Open Sans",Arial,sans-serif}
a{color:inherit;text-decoration:none}
.container{width:1002px;margin:0 auto;position:relative}

/* Hero */
.hero{position:relative;height:625px;overflow:hidden}
.hero-art{position:absolute;inset:0;background:
  radial-gradient(ellipse at 50% 40%,rgba(0,0,0,.55) 0%,rgba(0,0,0,.2) 60%,rgba(0,0,0,.55) 100%),
  linear-gradient(115deg,#1c2333 0%,#2d3a52 25%,#3b3f4a 45%,#2a3046 65%,#47404a 85%,#1a1d26 100%)}
.hero-fade{position:absolute;left:0;right:0;bottom:0;height:140px;background:linear-gradient(to bottom,rgba(20,20,20,0),var(--bg-a))}
.site-header{position:absolute;top:24px;left:0;right:0;z-index:2}
.site-header .container{display:flex;align-items:center;height:62px}
.brand{display:flex;align-items:center;gap:10px}
.brand-mark{width:34px;height:50px;background:var(--white)}
.brand-text{display:flex;flex-direction:column;line-height:1}
.brand-name{font-family:"Roboto",sans-serif;font-weight:500;font-size:34px;color:var(--red);letter-spacing:.5px}
.brand-tag{font-size:13px;color:var(--white);margin-top:3px;padding-left:68px}
.main-nav{margin-left:auto;display:flex;align-items:center;gap:26px;font-size:15px;font-weight:600}
.main-nav .caret{display:inline-block;width:0;height:0;border-left:5px solid transparent;border-right:5px solid transparent;border-top:6px solid var(--white);margin-left:5px;vertical-align:2px}
.nav-actions{display:flex;gap:10px;margin-left:24px}
.btn-outline{display:flex;align-items:center;gap:6px;height:44px;padding:0 14px;border:2px solid var(--red);border-radius:22px;font-family:"Roboto",sans-serif;font-weight:700;font-size:15px;text-transform:uppercase}
.hero-copy{position:absolute;top:210px;left:0;right:0;text-align:center;z-index:2}
.hero-title{font-family:"Roboto",sans-serif;font-weight:700;font-size:66px;letter-spacing:.5px;line-height:1}
.hero-sub{font-family:"Open Sans",sans-serif;font-weight:600;font-size:24px;margin-top:26px}
.btn-watch{display:inline-flex;align-items:center;justify-content:center;gap:14px;margin-top:36px;width:282px;height:74px;border-radius:37px;background:var(--red);font-family:"Roboto",sans-serif;font-weight:700;font-size:23px;text-transform:uppercase}

/* Rails */
.rail{background:var(--bg-a)}
.rail:nth-of-type(even){background:var(--bg-b)}
.rail-head{display:flex;align-items:flex-end;justify-content:space-between;height:69px;border-bottom:5px solid var(--red)}
.rail-title{height:69px;width:318px;background:var(--red);clip-path:polygon(0 0,88% 0,100% 100%,0 100%);display:flex;align-items:center;padding-left:27px;font-family:"Roboto",sans-serif;font-weight:700;font-size:33px;text-transform:uppercase}
.view-all{font-family:"Roboto",sans-serif;font-weight:700;font-size:17px;text-decoration:underline;text-transform:uppercase;margin-bottom:16px}
.grid{display:grid;grid-template-columns:repeat(4,235px);column-gap:20px;margin-top:48px}
.thumb{border:3px solid var(--white);border-radius:3px}
.card-title{font-family:"Roboto",sans-serif;font-weight:500;font-size:22px;margin-top:24px}
.card-time{font-size:14px;color:var(--text);margin-top:6px}

.rail-new{height:530px;padding-top:81px}
.rail-new .thumb{height:181px}
.rail-library{height:594px;padding-top:73px}
.rail-library .thumb{height:265px}
.rail-trailers{height:513px;padding-top:73px}
.rail-trailers .thumb{height:181px}
.rail-shorts{height:538px;padding-top:81px}
.rail-shorts .thumb{height:153px}

/* Footer */
.site-footer{background:var(--footer);height:432px;padding-top:60px}
.footer-cols{display:flex;height:268px}
.footer-col{list-style:none;font-size:15px;color:var(--text);line-height:29px}
.footer-col:nth-child(1){width:231px}
.footer-col:nth-child(2){width:239px}
.footer-col:nth-child(3){width:247px}
.apps-title{font-weight:700;font-size:16px;color:var(--white);margin-top:14px}
.app-btn{display:inline-flex;align-items:center;gap:8px;margin-top:12px;height:28px;padding:0 10px;background:#3a3a3a;border-radius:3px;font-size:12px;line-height:1}
.app-btn i{width:14px;height:14px;background:var(--muted)}
.footer-bottom{border-top:1px solid var(--rule);display:flex;align-items:center;justify-content:space-between;height:104px}
.copyright{font-size:14px;color:var(--text)}
.social{display:flex;gap:10px;list-style:none}
.social a{display:block;width:43px;height:43px;border:2px solid var(--white);border-radius:50%}
</style>
</head>
<body>

<header class="hero">
  <div class="hero-art" role="img" aria-label="Wall of glowing screens showing film stills fading into darkness"></div>
  <div class="hero-fade"></div>
  <div class="site-header">
    <div class="container">
      <a class="brand" href="#">
        <span class="brand-mark"></span>
        <span class="brand-text">
          <span class="brand-name">KALDORVUE</span>
          <span class="brand-tag">we screen your dreams</span>
        </span>
      </a>
      <nav class="main-nav">
        <a href="#">About Us</a>
        <a href="#">Movies<span class="caret"></span></a>
        <a href="#">Terms of Service</a>
        <a href="#">Contact</a>
        <a href="#" aria-label="Search">
          <svg width="16" height="16" viewBox="0 0 16 16"><circle cx="6.5" cy="6.5" r="5" fill="none" stroke="#fff" stroke-width="2.2"/><line x1="10.2" y1="10.2" x2="14.5" y2="14.5" stroke="#fff" stroke-width="2.6" stroke-linecap="round"/></svg>
        </a>
      </nav>
      <div class="nav-actions">
        <a class="btn-outline" href="#">
          <svg width="12" height="14" viewBox="0 0 12 14"><rect x="1" y="6" width="10" height="8" rx="1" fill="#fff"/><path d="M3 6V4a3 3 0 0 1 6 0v2" fill="none" stroke="#fff" stroke-width="2"/></svg>Login</a>
        <a class="btn-outline" href="#">
          <svg width="13" height="13" viewBox="0 0 13 13"><path d="M1 12l1-4 7-7 3 3-7 7z" fill="#fff"/></svg>Register</a>
      </div>
    </div>
  </div>
  <div class="hero-copy">
    <h1 class="hero-title">WE SCREEN YOUR DREAMS</h1>
    <p class="hero-sub">Online platform for the presentation of all visual art forms</p>
    <a class="btn-watch" href="#">
      <svg width="24" height="24" viewBox="0 0 24 24"><circle cx="12" cy="12" r="12" fill="#fff"/><path d="M9.5 7l7 5-7 5z" fill="#d0171b"/></svg>Watch Movie</a>
  </div>
</header>

<main>
  <section class="rail rail-new">
    <div class="container">
      <div class="rail-head"><h2 class="rail-title">New Releases</h2><a class="view-all" href="#">View All</a></div>
      <div class="grid">
        <article><div class="thumb" role="img" aria-label="Two cranes standing in a golden meadow" style="background:linear-gradient(180deg,#8f9a5c,#a8a35a 60%,#6f7440)"></div><h3 class="card-title">Finibus Bonoe Maloru</h3><p class="card-time">1m 30s</p></article>
        <article><div class="thumb" role="img" aria-label="Dancer in dark clothing against a black background" style="background:radial-gradient(circle at 55% 35%,#3a3a3a,#050505 70%)"></div><h3 class="card-title">Finibus Bonoe Maloru</h3><p class="card-time">1m 30s</p></article>
        <article><div class="thumb" role="img" aria-label="Bare winter trees under a grey sky" style="background:linear-gradient(180deg,#9a9592,#5a4a47 50%,#2b2220)"></div><h3 class="card-title">Finibus Bonoe Maloru</h3><p class="card-time">1m 30s</p></article>
        <article><div class="thumb" role="img" aria-label="City boulevard with palm trees at dusk" style="background:linear-gradient(180deg,#6c5a9a,#c4688a 55%,#3a2a40)"></div><h3 class="card-title">Finibus Bonoe Maloru</h3><p class="card-time">1m 30s</p></article>
      </div>
    </div>
  </section>

  <section class="rail rail-library">
    <div class="container">
      <div class="rail-head"><h2 class="rail-title">Library</h2><a class="view-all" href="#">View All</a></div>
      <div class="grid">
        <article><div class="thumb" role="img" aria-label="Musicians playing trumpet outdoors in sunlight" style="background:linear-gradient(160deg,#e8d9b0,#b59a68 55%,#5c4a30)"></div><h3 class="card-title">Finibus Bonoe Maloru</h3><p class="card-time">1m 30s</p></article>
        <article><div class="thumb" role="img" aria-label="Couple silhouetted in a field at sunset" style="background:radial-gradient(circle at 50% 55%,#ffd27a,#d08a2a 45%,#4a2a10)"></div><h3 class="card-title">Finibus Bonoe Maloru</h3><p class="card-time">1m 30s</p></article>
        <article><div class="thumb" role="img" aria-label="Costumed figure in a blue misty forest" style="background:linear-gradient(180deg,#3d5a8a,#2a3a5e 55%,#1a2036)"></div><h3 class="card-title">Finibus Bonoe Maloru</h3><p class="card-time">1m 30s</p></article>
        <article><div class="thumb" role="img" aria-label="Narrow lamp-lit alley at night" style="background:linear-gradient(180deg,#2a2416,#6a5526 50%,#1e1a10)"></div><h3 class="card-title">Finibus Bonoe Maloru</h3><p class="card-time">1m 30s</p></article>
      </div>
    </div>
  </section>

  <section class="rail rail-trailers">
    <div class="container">
      <div class="rail-head"><h2 class="rail-title">Trailers</h2><a class="view-all" href="#">View All</a></div>
      <div class="grid">
        <article><div class="thumb" role="img" aria-label="Hiker overlooking a mountain valley" style="background:linear-gradient(180deg,#c9d2dc,#8a8d8e 45%,#4a4a44)"></div><h3 class="card-title">Finibus Bonoe Maloru</h3><p class="card-time">1m 30s</p></article>
        <article><div class="thumb" role="img" aria-label="Director with megaphone on a bright beach, black and white" style="background:linear-gradient(180deg,#d8d8d8,#f2f2f2 60%,#bdbdbd)"></div><h3 class="card-title">Finibus Bonoe Maloru</h3><p class="card-time">1m 30s</p></article>
        <article><div class="thumb" role="img" aria-label="Forest road with sunbeams through trees" style="background:radial-gradient(circle at 55% 45%,#e8c87a,#8a7a3a 45%,#2e2a14)"></div><h3 class="card-title">Finibus Bonoe Maloru</h3><p class="card-time">1m 30s</p></article>
        <article><div class="thumb" role="img" aria-label="Aerial view of a winding road through snowy pines" style="background:linear-gradient(135deg,#4a5a40,#cfd4cc 50%,#3e4a38)"></div><h3 class="card-title">Finibus Bonoe Maloru</h3><p class="card-time">1m 30s</p></article>
      </div>
    </div>
  </section>

  <section class="rail rail-shorts">
    <div class="container">
      <div class="rail-head"><h2 class="rail-title">Shortfilms</h2><a class="view-all" href="#">View All</a></div>
      <div class="grid">
        <article><div class="thumb" role="img" aria-label="Lone figure walking in a dark green field" style="background:linear-gradient(180deg,#4a5550,#2e3a2c 55%,#1c221a)"></div><h3 class="card-title">Finibus Bonoe Maloru</h3><p class="card-time">1m 30s</p></article>
        <article><div class="thumb" role="img" aria-label="Car interior at night with blurred lights" style="background:radial-gradient(circle at 60% 60%,#d08a4a,#4a3a30 45%,#141414)"></div><h3 class="card-title">Finibus Bonoe Maloru</h3><p class="card-time">1m 30s</p></article>
        <article><div class="thumb" role="img" aria-label="Red car on a cliffside road at sunset" style="background:linear-gradient(160deg,#e0b07a,#8a6a5a 50%,#3a3436)"></div><h3 class="card-title">Finibus Bonoe Maloru</h3><p class="card-time">1m 30s</p></article>
        <article><div class="thumb" role="img" aria-label="Couple embracing in soft natural light" style="background:linear-gradient(135deg,#8a9a7a,#b89a7a 55%,#5a4636)"></div><h3 class="card-title">Finibus Bonoe Maloru</h3><p class="card-time">1m 30s</p></article>
      </div>
    </div>
  </section>
</main>

<footer class="site-footer">
  <div class="container">
    <div class="footer-cols">
      <ul class="footer-col">
        <li>Movies</li><li>Feature films</li><li>Short films</li><li>Documentaries</li><li>Game shows</li><li>Reality shows</li><li>Serials</li><li>Traditional art</li>
      </ul>
      <ul class="footer-col">
        <li>Subscription</li><li>Gift KALDORVUE</li><li>Devices</li><li>Originals</li>
      </ul>
      <ul class="footer-col">
        <li>About Us</li><li>Help Center</li><li>Contact Us</li><li>Blog</li><li>Investor Relations</li>
      </ul>
      <ul class="footer-col">
        <li>Unlimited Movies &amp; Music</li><li>On Your Favorite Devices</li><li>Hd, Sub-Titles, Playlists</li>
        <li class="apps-title">Download Apps</li>
        <li><a class="app-btn" href="#"><i></i>Handset</a></li>
      </ul>
    </div>
    <div class="footer-bottom">
      <p class="copyright">© 2018, KALDORVUE. All rights reserved.</p>
      <ul class="social">
        <li><a href="#" aria-label="Chatterly"></a></li>
        <li><a href="#" aria-label="quibbr"></a></li>
        <li><a href="#" aria-label="Snapgrove"></a></li>
      </ul>
    </div>
  </div>
</footer>

</body>
</html>
```